Coldforge Prime manufacturing Project

We are looking at getting a brand new design for a new company that deals in selling stainless tubing and other stainless still products such as handrails, Spigots, Balustrade Fittings
Glass, Glass fittings and Aluminium Channels

We require a very clean website that deals with the following colours:

Blue to light blues
Blacks
Greys to light Greys
Whites

We are open for other ideas BUT we *DO NOT* want any pinks, greens or bright colours except for backgrounds colours we have chosen above. (It can be solid, gradient or a subtle pattern)

YOU MUST KEEP THE LOGO AS IS. PLEASE DO NOT ALTER THE LOGO IN *ANY WAY* and the logo MUST be the same colours and fonts.

Logo is attached.

The site must contain these aspects:
jQuery Slider (Image slide show)
Top drop down Menus
Be no more than 900px wide
Text is to be to the w3C standards. (no special fonts)

We will chop up the design into html format. You just need to provide the PSD file.

The clients opposition is:
www.quorvatrim.example

Industry/Entity Type

It Company

Requirements
Nice to have
• Alter the logo in anyway

Files

```html
<!DOCTYPE html>
<html lang="en">
<head>
<meta charset="utf-8">
<title>Coldforge Prime – Home</title>
<link rel="stylesheet" href="https://fonts.googleapis.com/css2?family=Source+Sans+3:wght@300;400;600;700&display=swap">
<style>
:root{
  --bg:#f0f0f0;
  --page:#ffffff;
  --ink:#3a3a3a;
  --ink-soft:#666666;
  --line:#dddddd;
  --blue-top:#7d99c9;
  --blue-bottom:#4f6ea7;
  --news-blue:#3d5a8a;
  --footer:#3b3b3b;
  --steel-light:#e4e4e6;
  --steel-mid:#a9abb0;
}
*{box-sizing:border-box;margin:0;padding:0}
html,body{width:1200px;height:1168px;overflow:hidden}
body{background:var(--bg);font-family:"Source Sans 3",Arial,sans-serif;color:var(--ink);position:relative}
.page{position:absolute;left:69px;top:0;width:1063px;height:1090px;background:var(--page);box-shadow:0 0 6px rgba(0,0,0,.08)}
.abs{position:absolute}

/* header */
.brand{left:29px;top:20px;display:flex;align-items:center;gap:10px}
.brand-mark{width:100px;height:100px;border-radius:50%;background:#2b3a55}
.brand-name{font-size:25px;font-weight:400;color:#1f2a3c;line-height:1.05;width:190px}
.search{left:768px;top:23px;width:257px;height:34px;border:1px solid #cfcfcf;border-radius:5px;font-size:13px;font-style:italic;color:#9a9a9a;padding:8px 14px}
.search svg{position:absolute;right:10px;top:7px}
.nav{left:567px;top:76px;display:flex;align-items:center;font-size:19.5px;color:var(--ink)}
.nav a{color:inherit;text-decoration:none;padding:0 17px;border-left:1px solid #cfcfcf;line-height:20px}
.nav .home{border:none;padding:0 17px 0 0;display:flex}

/* hero */
.hero-photo{left:0;top:130px;width:665px;height:390px;background:radial-gradient(ellipse at 55% 45%,#f2f2f3 0%,#c9cacd 55%,#9d9fa3 100%)}
.hero-panel{left:665px;top:130px;width:400px;height:390px;background:linear-gradient(180deg,var(--blue-top),var(--blue-bottom));color:#fff;padding:57px 33px 0 33px}
.hero-kicker{font-size:31px;font-weight:300;line-height:1.1}
.hero-title{font-size:41px;font-weight:600;line-height:1.2;margin-top:2px}
.hero-text{font-size:15px;line-height:26px;margin-top:12px;color:#eef2fa;width:300px}
.dots{display:flex;gap:6px;margin-top:18px}
.dots span{width:15px;height:15px;border-radius:50%;background:#fff}
.dots span.active{background:transparent;border:2px solid #fff}

/* categories */
.category{top:550px;width:218px}
.category-photo{height:113px}
.category h3{font-size:21px;font-weight:600;margin-top:9px;color:var(--ink)}
.category p{font-size:14.5px;line-height:21px;color:var(--ink-soft);margin-top:2px}
.col-rule{top:550px;height:198px;border-left:1px dotted #bbbbbb}
.divider{left:36px;top:796px;width:992px;border-top:1px solid var(--line)}

/* about */
.about-photo{left:28px;top:828px;width:206px;height:190px;border:1px solid #d8d8d8;border-radius:6px;background:linear-gradient(160deg,#f4f4f5,#b8babe 60%,#e2e3e5)}
.about{left:253px;top:824px;width:420px}
.about h2{font-size:28px;font-weight:400;color:var(--ink)}
.about h4{font-size:17px;font-weight:400;margin-top:6px;color:var(--ink)}
.about p{font-size:14.5px;line-height:26px;color:var(--ink-soft);margin-top:4px}
.news{left:717px;top:824px;width:320px}
.news h2{font-size:23px;font-weight:600;color:var(--news-blue)}
.news-item{margin-top:10px}
.news-item h5{font-size:16.5px;font-weight:400;color:var(--news-blue)}
.news-item p{font-size:14px;color:var(--ink-soft);margin-top:1px}
.news-more{display:block;margin-top:16px;font-size:12.5px;font-weight:700;color:#222;text-decoration:none}

/* footer */
.footer{left:0;top:1090px;width:1200px;height:78px;background:var(--footer);color:#fff}
.copyright{left:100px;top:26px;font-size:13px;color:#bdbdbd}
.footer-nav{left:627px;top:25px;display:flex;gap:19px;font-size:16px}
.footer-nav a{color:#fff;text-decoration:none}
.social{left:1034px;top:26px;display:flex;gap:8px}
.social span{width:22px;height:22px;border-radius:50%;background:#ffffff}
</style>
</head>
<body>
<div class="page">
  <header>
    <div class="abs brand">
      <span class="brand-mark"></span>
      <span class="brand-name">Coldforge Prime Metal Works Co. Ltd</span>
    </div>
    <div class="abs search">Search here
      <svg width="20" height="20" viewBox="0 0 20 20"><circle cx="8" cy="8" r="6" fill="none" stroke="#9a9a9a" stroke-width="2.4"/><line x1="12.5" y1="12.5" x2="18" y2="18" stroke="#9a9a9a" stroke-width="3" stroke-linecap="round"/></svg>
    </div>
    <nav class="abs nav">
      <a class="home" href="#" aria-label="Home"><svg width="26" height="24" viewBox="0 0 26 24"><path d="M13 1 L25 12 H21 V23 H5 V12 H1 Z" fill="#111"/><rect x="11" y="15" width="4" height="8" fill="#fff"/></svg></a>
      <a href="#">About Us</a><a href="#">Products</a><a href="#">Download</a><a href="#">Contact</a>
    </nav>
  </header>

  <section>
    <div class="abs hero-photo" role="img" aria-label="Polished stainless steel pipe fittings: elbows, tees and reducers"></div>
    <div class="abs hero-panel">
      <div class="hero-kicker">Welcome to Our</div>
      <div class="hero-title">Website Mainpage</div>
      <p class="hero-text">Nunc tempus felis vitae urna. Vivamus porttitor, g, purus nisi eleifend libero, a tempus libero lectus feugiat felis. Morbi diam mauris, viverra in, gravida eu, mattis in, ante.</p>
      <div class="dots"><span class="active"></span><span></span><span></span><span></span></div>
    </div>
  </section>

  <section>
    <div class="abs category" style="left:28px">
      <div class="category-photo" role="img" aria-label="Staircase with wrought metal handrail" style="background:linear-gradient(135deg,#d8c8a8,#8a7a62)"></div>
      <h3>Handrails</h3><p>Phasellus felis dolor, scelerisque a, tempus eget</p>
    </div>
    <div class="abs col-rule" style="left:261px"></div>
    <div class="abs category" style="left:281px">
      <div class="category-photo" role="img" aria-label="Chrome kitchen spigot pouring water" style="background:linear-gradient(135deg,#c9cbcf,#6f7378)"></div>
      <h3>Spigots</h3><p>Nunc tempus felis vitae urna. Vivamus porttitor purus nisi eleifend</p>
    </div>
    <div class="abs col-rule" style="left:522px"></div>
    <div class="abs category" style="left:549px">
      <div class="category-photo" role="img" aria-label="Stainless balustrade with horizontal rails" style="background:linear-gradient(135deg,#b9bcc2,#6c7079)"></div>
      <h3>Balustrade Fittings</h3><p>Phasellus felis dolor, scelerisque a, tempus eget lobortis id</p>
    </div>
    <div class="abs col-rule" style="left:791px"></div>
    <div class="abs category" style="left:816px">
      <div class="category-photo" role="img" aria-label="Workers installing a large glass facade" style="background:linear-gradient(135deg,#9fb4dc,#4d6aa6)"></div>
      <h3>Glass fittings</h3><p>Phasellus felis dolor, scelerisque a, tempus eget, lobortis id</p>
    </div>
    <div class="abs divider"></div>
  </section>

  <section>
    <div class="abs about-photo" role="img" aria-label="Stack of aluminium tubes and channels"></div>
    <div class="abs about">
      <h2>About Our Products</h2>
      <h4>Duis tincidunt lectus quis dui viverra vestibulum.</h4>
      <p>Maecenas placerat, nisl at consequat rhoncus, sem nunc gravida justo, quis eleifend arcu velit quis lacus. Morbi magna magna, tincidunt a, mattis non, imperdiet vitae, tellus. Sed odio est, auctor ac, sollicitudin in, consequat vitae, orci. Fusce id felis. Vivamus sollicitudin metus eget eros.</p>
    </div>
    <div class="abs news">
      <h2>Latest News &amp; Projects</h2>
      <div class="news-item"><h5>Duis tincidunt lectus quis dui</h5><p>Maecenas placerat, nisl at consequat rhoncus sem</p></div>
      <div class="news-item"><h5>Maecenas aliquet velit vel turpis</h5><p>Mauris neque metus, malesuada nec ultricies sit amet</p></div>
      <a class="news-more" href="#">VIEW MORE NEWS</a>
    </div>
  </section>
</div>

<footer class="abs footer">
  <div class="abs copyright">© 2013 Company Name.&nbsp; All right reserved.&nbsp; Term of Use</div>
  <nav class="abs footer-nav"><a href="#">Main</a><a href="#">About Us</a><a href="#">Our Services</a><a href="#">Products</a><a href="#">Contact Us</a></nav>
  <div class="abs social" aria-label="Social links"><span></span><span></span><span></span></div>
</footer>
</body>
</html>
```